ESPDT Flyer to promote our services in the PVT Event in Nashville, TN

Please use our website at www.sunnysprout-kids.com to get our color seem and details about our program to design a flyer. This is exclusively for our EPSDT service not clinics or optometry.
SSI Mission Statement
Larkfield Holdings, LLC, dba, "Sunny Sprout" feels a strong sense of connection to entities whose mission is to improve the educational achievements of students. In a similar way, Sunny Sprout is committed to improving the health of children by providing healthcare to students and in a school-based setting. We work to keep children healthy, ready to learn and in the classroom.
We believe that undiagnosed and untreated health problems can become barriers to a child's ability to learn. We believe that preventive health services, in the school setting, reduce or eliminate barriers to healthcare. We believe that diversity is to be valued and respected.
It is Sunny Sprout's desire provide the Annual health exams / Sports physicals and Optometry services to your students.
Description of Services
Annual Health Screening
These annual screenings and sports physicals will comply with the Early Periodic Screening, Diagnosis and Treatment (EPSDT) as mandated by the Tennessee Medicaid program. The intent of the EPSDT program is to identify problems at birth (Early), to check health status at different intervals (Periodic), provide services that will identify health issues (Screening) that lead to classification of health issues (Diagnosis and follow-up), and elimination or provide ongoing care for diagnosed health problems (Treatment).
Sunny Sprout transports a portable and well-equipped clinic to each school site. Sunny Sprout's practitioners diagnose medical illnesses and make referrals to the child’s primary care provider (PCP). The clinical teams consist of a Nurse Practitioner and three support team members.
This service is at No out-of-pocket Cost to the school district or parent. We bill insurances.
Target Market(s)
Coordinated School Healthcare Professinals
Industry/Entity Type
Health And Wellness
Requirements
Must have
- Must have description of the EPSDT exam
Nice to have
- Picture of diversity: Children and Nurses

```html
<!DOCTYPE html>
<html lang="en">
<head>
<meta charset="utf-8">
<title>Sunny Sprout – Annual Health Screening Flyer</title>
<link href="https://fonts.googleapis.com/css2?family=Tinos:ital,wght@0,400;0,700;1,400&display=swap" rel="stylesheet">
<style>
  :root {
    --page-bg: #e6e6e6;
    --paper: #ffffff;
    --paper-shade: #eeeff1;
    --brand-blue: #1a5cae;
    --brand-deep: #0c3f91;
    --brand-light: #5a8fd0;
    --ink: #1d1d1d;
    --ink-soft: #2a2a2a;
  }
  * { box-sizing: border-box; margin: 0; padding: 0; }
  html, body {
    width: 1125px; height: 1200px; overflow: hidden;
    background: var(--page-bg);
    font-family: "Tinos", "Times New Roman", serif;
  }
  .flyer {
    position: absolute; left: 112px; top: 18px;
    width: 900px; height: 1164px;
    background: linear-gradient(180deg, var(--paper) 0%, var(--paper) 22%, var(--paper-shade) 26%, var(--paper-shade) 50%, var(--paper) 70%);
    overflow: hidden;
    box-shadow: 0 2px 10px rgba(0,0,0,.18);
  }

  .header-band {
    position: absolute; left: 0; top: 250px; width: 900px; height: 40px;
    background: linear-gradient(180deg, var(--brand-blue) 0%, var(--brand-blue) 65%, var(--brand-deep) 65%, var(--brand-deep) 100%);
  }

  .brand { position: absolute; left: 52px; top: 50px; }
  .brand-name {
    display: flex; align-items: center; gap: 12px;
    font-size: 54px; font-weight: 400; color: var(--brand-blue);
    line-height: 1; letter-spacing: -0.5px;
  }
  .brand-mark {
    width: 22px; height: 22px; border-radius: 50%;
    background: var(--brand-blue);
  }
  .brand-tagline {
    margin-top: 12px; margin-left: 8px;
    font-size: 20px; color: var(--brand-blue);
  }

  .site-url {
    position: absolute; right: 30px; top: 54px;
    font-size: 20px; color: var(--ink-soft);
  }
  .slogan {
    position: absolute; right: 30px; top: 92px;
    text-align: right; font-style: italic; color: var(--brand-blue);
    line-height: 1.15;
  }
  .slogan-line-1 { font-size: 42px; }
  .slogan-line-1 .slogan-small { font-size: 32px; }
  .slogan-line-2 { font-size: 48px; padding-top: 4px; }

  .screening {
    position: absolute; left: 50px; top: 318px; width: 800px;
    text-align: center; color: var(--ink);
  }
  .screening-title { font-size: 34px; font-weight: 700; margin-bottom: 18px; }
  .screening-text { font-size: 19.4px; line-height: 23.5px; margin-bottom: 16px; }
  .screening-note {
    font-size: 22px; font-weight: 700; line-height: 35px; margin-top: 12px;
  }

  .children-photo {
    position: absolute; left: 30px; top: 770px; width: 840px; height: 394px;
    background: linear-gradient(90deg, #c8e27a 0%, #f3d2b6 22%, #e46aa8 45%, #f0cf5b 65%, #9fd3ee 88%);
    opacity: .85;
  }
</style>
</head>
<body>
  <main class="flyer">
    <div class="header-band" role="img" aria-label="Decorative blue header band"></div>

    <div class="brand">
      <div class="brand-name"><span class="brand-mark"></span>Sunny Sprout</div>
      <div class="brand-tagline">Innovators in School Health Care Services</div>
    </div>

    <div class="site-url">www.sunnysprout-kids.com</div>
    <div class="slogan">
      <div class="slogan-line-1">Healthy Bodies <span class="slogan-small">Promote</span></div>
      <div class="slogan-line-2">Healthy Minds</div>
    </div>

    <section class="screening">
      <h1 class="screening-title">Annual Health Screening</h1>
      <p class="screening-text">These annual screenings and sports physicals will comply with the Early Periodic Screening,<br>Diagnosis and Treatment (EPSDT) as mandated by the Tennessee Medicaid program.<br>The intent of the EPSDT program is to identify problems at birth (Early), to check health<br>status at different intervals (Periodic), provide services that will identify health issues<br>(Screening) that lead to classification of health issues (Diagnosis and follow-up), and<br>elimination or provide ongoing care for diagnosed health problems (Treatment).</p>
      <p class="screening-text">Sunny Sprout transports a portable and well-equipped clinic to each school site. Sunny Sprout's<br>practitioners diagnose medical illnesses and make referrals to the child’s primary care<br>provider (PCP). The clinical teams consist of a Nurse<br>Practitioner and three support team members.</p>
      <p class="screening-note">This service is at No out-of-pocket Cost to the school district or parent.<br>We bill insurances.</p>
    </section>

    <div class="children-photo" role="img" aria-label="Photo of five smiling, diverse young children standing together in colorful clothes in front of a blue wave backdrop"></div>
  </main>
</body>
</html>
```